Facebook Ad design

We need designed a Facebook ad for our solar system's. We want to advertise a 13.32kW system for $4499.

Including: Velmor Falcon QX 370W Panels and Pelmara inverters.

```html
<!DOCTYPE html>
<html lang="en">
<head>
<meta charset="utf-8">
<title>Solvane Power – Solar System Facebook Ad</title>
<link rel="stylesheet" href="https://fonts.googleapis.com/css2?family=Libre+Baskerville:wght@700&family=Lato:wght@300;400;700&display=swap">
<style>
  :root {
    --brand-red: #c01e2e;
    --brand-navy: #2e3447;
    --soft-grey: #8c8c8c;
    --light-grey: #9a9a9a;
    --paper: #ffffff;
    --backdrop: #e9e9eb;
    --serif: "Libre Baskerville", Georgia, serif;
    --sans: "Lato", Arial, sans-serif;
  }
  * { box-sizing: border-box; margin: 0; padding: 0; }
  html, body { width: 1200px; height: 815px; overflow: hidden; background: var(--backdrop); }
  .ad {
    position: absolute; left: 220px; top: 28px;
    width: 760px; height: 760px;
    background: var(--paper);
    overflow: hidden;
    font-family: var(--sans);
  }
  .ad__shapes { position: absolute; inset: 0; }
  .brand { position: absolute; left: 27px; top: 40px; }
  .brand__name {
    display: flex; align-items: center; gap: 12px;
    font-family: var(--sans); font-weight: 700; color: var(--brand-navy);
    font-size: 32px; line-height: 1; letter-spacing: 1px;
  }
  .brand__mark { width: 24px; height: 24px; background: var(--brand-red); flex: none; }
  .brand__tagline {
    margin-top: 12px; font-size: 12.5px; color: var(--brand-navy);
    letter-spacing: 0.4px; font-weight: 400;
  }
  .product-title {
    position: absolute; left: 28px; top: 232px;
    font-family: var(--serif); font-weight: 700;
    font-size: 50px; line-height: 50px;
  }
  .product-title__line--dark { color: var(--brand-navy); display: block; }
  .product-title__line--red { color: var(--brand-red); display: block; }
  .new-badge {
    position: absolute; right: 16px; top: 200px; text-align: right;
    font-weight: 300; color: var(--light-grey);
    font-size: 41px; line-height: 52px;
  }
  .item-label {
    position: absolute; text-align: center; color: var(--soft-grey);
    font-weight: 400; transform: translate(-50%, -50%); white-space: nowrap;
  }
  .item-label--panels { left: 448px; top: 366px; font-size: 18px; line-height: 28px; }
  .item-label--inverters { left: 567px; top: 535px; font-size: 14px; line-height: 22px; }
  .price {
    position: absolute; left: 29px; top: 453px; width: 301px; height: 109px;
    background: var(--brand-navy); color: var(--paper);
    font-family: var(--serif); font-weight: 700;
  }
  .price__currency { position: absolute; left: 8px; top: 6px; font-size: 44px; line-height: 1; }
  .price__amount { position: absolute; left: 40px; top: -4px; font-size: 88px; line-height: 1.2; letter-spacing: 1px; }
  .offer-tag {
    position: absolute; left: 37px; top: 556px; width: 187px; height: 31px;
    background: var(--brand-red); color: var(--paper);
    font-weight: 700; font-size: 22px; line-height: 31px; text-align: center;
  }
  .order-button {
    position: absolute; left: 30px; top: 695px; width: 215px; height: 41px;
    background: var(--brand-red); color: var(--paper); border-radius: 21px;
    box-shadow: 4px 4px 0 var(--brand-navy);
    font-size: 21px; line-height: 41px; text-align: center; font-weight: 400;
  }
  .web-address {
    position: absolute; right: 22px; top: 705px;
    font-size: 21px; letter-spacing: 4.5px; color: var(--brand-navy); font-weight: 400;
  }
</style>
</head>
<body>
  <main class="ad">
    <svg class="ad__shapes" width="760" height="760" viewBox="0 0 760 760" aria-hidden="true">
      <polyline points="595,-6 315,291 355,314" fill="none" stroke="var(--brand-red)" stroke-width="20" stroke-linejoin="miter"/>
      <polygon points="439,235 581,360 457,499 315,377" fill="none" stroke="var(--brand-navy)" stroke-width="8" stroke-linejoin="miter"/>
      <rect x="512" y="445" width="16" height="16" fill="var(--brand-red)" transform="rotate(40 520 453)"/>
      <polygon points="561,438 663,527 573,633 470,541" fill="none" stroke="var(--brand-navy)" stroke-width="7" stroke-linejoin="miter"/>
      <polyline points="640,576 669,598 770,465" fill="none" stroke="var(--brand-red)" stroke-width="20" stroke-linejoin="miter"/>
    </svg>

    <header class="brand">
      <div class="brand__name"><span class="brand__mark"></span>SOLVANE POWER</div>
      <p class="brand__tagline">CLEAN SOLAR SYSTEMS FOR EVERY HOME</p>
    </header>

    <h1 class="product-title">
      <span class="product-title__line--dark">PRODUCT</span>
      <span class="product-title__line--red">NAME</span>
    </h1>

    <p class="new-badge">NEW<br>PRODUCT</p>

    <p class="item-label item-label--panels">VELMOR FALCON QX<br>370W PANELS</p>
    <p class="item-label item-label--inverters">PELMARA<br>INVERTERS</p>

    <div class="price">
      <span class="price__currency">$</span>
      <span class="price__amount">4499</span>
    </div>
    <div class="offer-tag">SPECIAL OFFER</div>

    <div class="order-button">ORDER NOW</div>
    <p class="web-address">WWW.WEBSITE.COM</p>
  </main>
</body>
</html>
```